Harbor Business Cards

I need a business card designed with the following information.

Company Name: Harbor Wealth Management
Name: BriAnne Dockery
Title: Executive Assistant
Cell: (503) 555-0173
Direct Line: (971) 555-0148
Email: brianne@harborwmx.com
Address: 20537 W. Marlowe PKWY Ste. B
Cedar Bluff, OR 97390

I have attached the logo.
I would like it in navy blue and silver.
Thanks.

```html
<!DOCTYPE html>
<html lang="en">
<head>
<meta charset="utf-8">
<title>Harbor Wealth Management – Business Card</title>
<link href="https://fonts.googleapis.com/css2?family=Lato:ital,wght@0,400;0,700;1,400&display=swap" rel="stylesheet">
<style>
  :root {
    --navy: #1d4670;
    --navy-deep: #133456;
    --navy-light: #2a5b8a;
    --silver: #c9ccd1;
    --silver-light: #e6e8eb;
    --paper: #fbfbfb;
    --backdrop: #e9eaec;
    --ink-light: #f3f5f8;
  }
  * { margin: 0; padding: 0; box-sizing: border-box; }
  html, body { width: 1200px; height: 900px; overflow: hidden; }
  body {
    background: var(--backdrop);
    font-family: "Lato", Arial, sans-serif;
    position: relative;
  }
  .card {
    position: absolute;
    left: 250px;
    width: 700px;
    height: 400px;
    overflow: hidden;
    box-shadow: 0 6px 18px rgba(0,0,0,0.18);
  }
  .card--back {
    top: 30px;
    background: radial-gradient(ellipse at 50% 35%, var(--navy-light) 0%, var(--navy) 55%, var(--navy-deep) 100%);
    display: flex;
    align-items: center;
    justify-content: center;
  }
  .wordmark {
    display: flex;
    flex-direction: column;
    align-items: center;
    gap: 14px;
    font-weight: 400;
    text-transform: uppercase;
    text-align: center;
  }
  .wordmark__dot { width: 18px; height: 18px; border-radius: 50%; }
  .wordmark__name {
    font-size: 40px;
    letter-spacing: 0.32em;
    line-height: 1;
    padding-left: 0.32em;
  }
  .wordmark__sub {
    font-size: 15px;
    letter-spacing: 0.3em;
    padding-left: 0.3em;
  }
  .card--back .wordmark { color: var(--silver); }
  .card--back .wordmark__dot { background: var(--silver); }

  .card--front {
    top: 470px;
    background: var(--paper);
  }
  .front-wave { position: absolute; inset: 0; }
  .card--front .wordmark {
    position: absolute;
    right: 40px;
    top: 78px;
    width: 340px;
    color: var(--navy);
  }
  .card--front .wordmark__name { font-size: 34px; }
  .card--front .wordmark__sub { font-size: 12px; }
  .card--front .wordmark__dot { background: var(--navy); }

  .contact {
    position: absolute;
    left: 46px;
    top: 150px;
    color: var(--ink-light);
  }
  .contact__name { font-size: 22px; font-weight: 700; line-height: 1.1; }
  .contact__title { font-size: 15px; font-style: italic; margin-bottom: 18px; }
  .contact__address { font-size: 15px; line-height: 1.3; margin-bottom: 12px; }
  .contact__list { list-style: none; font-size: 15px; line-height: 1.45; }
  .contact__list li { display: flex; align-items: center; gap: 10px; }
  .contact__list svg { width: 13px; height: 13px; flex: none; }
</style>
</head>
<body>

<section class="card card--back" aria-label="Card back">
  <div class="wordmark">
    <span class="wordmark__dot"></span>
    <span class="wordmark__name">Harbor</span>
    <span class="wordmark__sub">Wealth Management</span>
  </div>
</section>

<section class="card card--front" aria-label="Card front">
  <svg class="front-wave" viewBox="0 0 700 400" preserveAspectRatio="none" aria-hidden="true">
    <defs>
      <linearGradient id="waveNavy" x1="0" y1="0" x2="1" y2="1">
        <stop offset="0" stop-color="#2a5b8a"/>
        <stop offset="1" stop-color="#173c62"/>
      </linearGradient>
    </defs>
    <path d="M0,400 L0,300 C200,340 420,360 700,300 L700,400 Z" fill="var(--silver)"/>
    <path d="M0,112 C150,72 270,120 370,232 C460,330 580,368 700,332 L700,400 L0,400 Z" fill="url(#waveNavy)"/>
    <path d="M300,138 C360,165 390,200 430,245 C500,318 590,350 700,320 L700,338 C590,368 490,340 420,262 C380,218 350,175 300,138 Z" fill="var(--silver-light)"/>
    <path d="M300,138 C360,160 395,195 440,245" stroke="#ffffff" stroke-width="3" fill="none"/>
  </svg>

  <div class="wordmark">
    <span class="wordmark__dot"></span>
    <span class="wordmark__name">Harbor</span>
    <span class="wordmark__sub">Wealth Management</span>
  </div>

  <div class="contact">
    <p class="contact__name">BriAnne Dockery</p>
    <p class="contact__title">Executive Assistant</p>
    <p class="contact__address">20537 W. Marlowe PKWY Ste. B<br>Cedar Bluff, OR 97390</p>
    <ul class="contact__list">
      <li><svg viewBox="0 0 16 16" fill="currentColor"><path d="M3 1l3 3-1.5 2a9 9 0 0 0 5.5 5.5L12 10l3 3-2 2C7 15 1 9 1 3z"/></svg>(503) 555-0173</li>
      <li><svg viewBox="0 0 16 16" fill="currentColor"><rect x="4" y="1" width="8" height="4"/><rect x="1" y="6" width="14" height="6" rx="1"/><rect x="4" y="10" width="8" height="5"/></svg>(971) 555-0148</li>
      <li><svg viewBox="0 0 16 16" fill="none" stroke="currentColor" stroke-width="1.5"><rect x="1" y="3" width="14" height="10"/><path d="M1 3l7 6 7-6"/></svg>brianne@harborwmx.com</li>
      <li><svg viewBox="0 0 16 16" fill="none" stroke="currentColor" stroke-width="1.4"><circle cx="8" cy="8" r="7"/><ellipse cx="8" cy="8" rx="3" ry="7"/><path d="M1 8h14"/></svg>www.harborwmx.com</li>
    </ul>
  </div>
</section>

</body>
</html>
```